Banner Design

We need a banner to display at various locations around the community to promote our gymnastics club. Please see our plumivox page for more photos.

It should be horizontal 76cm X 183cm

```html
<!DOCTYPE html>
<html lang="en">
<head>
<meta charset="utf-8">
<title>Vaultline Gymsports Banner</title>
<link rel="stylesheet" href="https://fonts.googleapis.com/css2?family=Teko:wght@600&family=Montserrat:wght@600;800&display=swap">
<style>
  :root {
    --lime: #a9bb15;
    --lime-pale: #dbe39a;
    --navy: #1f2b6c;
    --white: #ffffff;
    --stage: #e8eaed;
    --photo-a: #3a62b8;
    --photo-b: #c9d3e6;
  }
  * { margin: 0; padding: 0; box-sizing: border-box; }
  html, body { width: 1200px; height: 849px; overflow: hidden; background: var(--stage); }
  .banner { position: absolute; left: 0; top: 175px; width: 1200px; height: 498px; overflow: hidden; background: var(--white); }
  .banner-art { position: absolute; inset: 0; }
  .headline {
    position: absolute; right: 604px; top: 50px; text-align: right;
    font-family: "Teko", sans-serif; font-weight: 600; font-size: 74px; line-height: 62px;
    color: var(--navy); letter-spacing: 1px;
  }
  .programs {
    position: absolute; left: 648px; top: 52px; list-style: none;
    font-family: "Montserrat", sans-serif; font-weight: 800; font-size: 20px; line-height: 28px;
    color: var(--navy);
  }
  .programs li { position: relative; }
  .programs li::before { content: "★"; position: absolute; left: -24px; top: 0; font-size: 14px; color: var(--lime); }
  .enrol-note {
    position: absolute; left: 418px; top: 346px;
    font-family: "Montserrat", sans-serif; font-weight: 600; font-size: 13px; color: var(--navy);
  }
  .brand { position: absolute; left: 412px; top: 380px; width: 170px; text-align: center; color: var(--navy); }
  .brand-name { font-family: "Montserrat", sans-serif; font-weight: 800; font-size: 28px; line-height: 30px; display: block; }
  .brand-sub { font-family: "Montserrat", sans-serif; font-weight: 800; font-size: 14px; letter-spacing: 3px; display: block; }
  .brand-web { font-family: "Montserrat", sans-serif; font-weight: 600; font-size: 11px; display: block; margin-top: 10px; }
  .contact { position: absolute; left: 594px; top: 372px; color: var(--navy); font-family: "Montserrat", sans-serif; font-weight: 800; }
  .contact-row { display: flex; align-items: center; gap: 10px; }
  .contact-row svg { flex: none; }
  .contact-phone { font-size: 40px; line-height: 48px; }
  .contact-small { font-size: 20px; line-height: 30px; }
</style>
</head>
<body>
<div class="banner">
  <svg class="banner-art" width="1200" height="498" viewBox="0 0 1200 498">
    <defs>
      <linearGradient id="photoTone" x1="0" y1="0" x2="0" y2="1">
        <stop offset="0" stop-color="var(--photo-b)"/>
        <stop offset="1" stop-color="var(--photo-a)"/>
      </linearGradient>
    </defs>
    <!-- pale stars behind headline and list -->
    <polygon class="star-bg" fill="var(--lime-pale)" points="470,10 520,0 600,10 615,337 470,337 420,180 280,40"/>
    <polygon class="star-bg" fill="var(--lime-pale)" points="650,10 760,10 975,40 850,150 880,337 700,337"/>
    <!-- lime left field -->
    <path fill="var(--lime)" d="M0,0 H120 C60,60 30,160 60,260 C90,330 200,380 330,410 C380,420 410,430 420,498 H0 Z"/>
    <path fill="var(--navy)" d="M0,360 C120,380 250,420 330,470 L300,498 L0,498 Z"/>
    <path fill="var(--lime)" d="M0,380 C100,400 200,430 260,470 L240,498 L0,498 Z"/>
    <path fill="var(--navy)" d="M90,150 C180,130 260,170 300,240 C220,220 150,210 90,230 Z"/>
    <!-- lime right field -->
    <path fill="var(--lime)" d="M1200,0 H1080 C1120,60 1150,160 1120,260 C1080,330 1000,340 900,337 V498 H1200 Z"/>
    <path fill="var(--navy)" d="M950,230 C1050,200 1140,150 1200,140 V220 C1120,240 1040,270 950,280 Z"/>
    <path fill="var(--navy)" d="M920,337 C1000,330 1100,300 1200,270 V300 C1120,330 1040,345 960,350 Z"/>
    <!-- bottom info band -->
    <path fill="var(--lime)" d="M360,337 H1200 V498 H360 Z"/>
    <line x1="360" y1="337" x2="1200" y2="337" stroke="var(--navy)" stroke-width="3"/>
    <!-- divider bar -->
    <rect x="619" y="3" width="15" height="334" fill="var(--navy)"/>
    <!-- photo circles -->
    <g stroke="var(--white)" stroke-width="5" fill="url(#photoTone)">
      <circle cx="123" cy="94" r="92" role="img" aria-label="Photo of a gymnast on the bars above a red crash mat"/>
      <circle cx="299" cy="198" r="92" role="img" aria-label="Photo of boys team wearing medals"/>
      <circle cx="120" cy="307" r="92" role="img" aria-label="Photo of the gym hall with a kinder gym circuit"/>
      <circle cx="299" cy="402" r="92" role="img" aria-label="Photo of a gymnast leaping on the beam"/>
      <circle cx="1073" cy="91" r="92" role="img" aria-label="Photo of the cheerleading squad with banners"/>
      <circle cx="924" cy="221" r="92" role="img" aria-label="Photo of a gymnast in a backbend on the floor"/>
      <circle cx="1073" cy="354" r="92" role="img" aria-label="Photo of a gymnast holding a standing split"/>
    </g>
  </svg>

  <h1 class="headline">JOIN<br>IN THE<br>FUN!</h1>

  <ul class="programs">
    <li>RECREATIONAL GYM</li>
    <li>COMPETITIVE GYM</li>
    <li>BOYS PROGRAMS</li>
    <li>CHEERLEADING</li>
    <li>KINDER GYM</li>
    <li>TUMBLING</li>
    <li>PARKOUR</li>
    <li>TRICKING</li>
  </ul>

  <p class="enrol-note">For enrolment details and further information on these and more classes visit</p>

  <div class="brand">
    <span class="brand-name">VAULTLINE</span>
    <span class="brand-sub">GYMSPORTS</span>
    <span class="brand-web">www.vaultlinegym.com</span>
  </div>

  <div class="contact">
    <div class="contact-row contact-phone">
      <svg width="18" height="18" viewBox="0 0 24 24" aria-hidden="true"><circle cx="12" cy="12" r="12" fill="var(--navy)"/><path d="M8 6l2 0 1 3-1.5 1c.7 1.6 2 2.9 3.5 3.5l1-1.5 3 1v2c0 1-1 2-2 2C10 17 7 14 7 8c0-1 .5-2 1-2z" fill="var(--lime)"/></svg>
      <span>(02) 5550 1827</span>
    </div>
    <div class="contact-row contact-small">
      <svg width="18" height="18" viewBox="0 0 24 24" aria-hidden="true"><circle cx="12" cy="12" r="12" fill="var(--navy)"/><rect x="6" y="8" width="12" height="8" rx="1" fill="var(--lime)"/><path d="M6 8l6 5 6-5" stroke="var(--navy)" stroke-width="1.5" fill="none"/></svg>
      <span>info@vaultlinegym.com</span>
    </div>
    <div class="contact-row contact-small">
      <svg width="18" height="18" viewBox="0 0 24 24" aria-hidden="true"><path d="M12 1C7 1 4 5 4 9c0 6 8 14 8 14s8-8 8-14c0-4-3-8-8-8z" fill="var(--navy)"/><circle cx="12" cy="9" r="3" fill="var(--lime)"/></svg>
      <span>42 Marden Pl, Kelby NSW 2199</span>
    </div>
  </div>
</div>
</body>
</html>
```